Stationary design for real estate company in Trinidad and Tobago

Kestra Realty Ltd. , real estate company operating in Trinidad and Tobago, requires a sleek, modern and professional stationary package to wow our customers and potential new clients. we want to look sleek and professional; first impressions count in this business!
Business Address:
Level 1, Marlowe Point Tower
4C Seldon Grove Boulevard
Marlowe Point
Colwyn Pereira Highway
Port of Spain
Trinidad
Tel: + 1 868 555 0147
www.kestra-tt.com
info@kestra-tt.com

```html
<!DOCTYPE html>
<html lang="en">
<head>
<meta charset="utf-8">
<title>Kestra Realty – Presentation Folder</title>
<link href="https://fonts.googleapis.com/css2?family=Montserrat:ital,wght@0,400;0,500;1,400&display=swap" rel="stylesheet">
<style>
  :root {
    --navy: #1c3a68;
    --navy-deep: #14305c;
    --gold: #c4a96b;
    --gold-light: #dcc38c;
    --paper: #ffffff;
    --paper-shade: #eef1f5;
    --ink: #1c2a44;
    --backdrop: #d9dbdf;
  }
  * { box-sizing: border-box; margin: 0; padding: 0; }
  html, body { width: 1200px; height: 1200px; overflow: hidden; }
  body {
    background: var(--backdrop);
    font-family: "Montserrat", sans-serif;
    color: var(--ink);
    display: flex;
    flex-direction: column;
    align-items: center;
    justify-content: center;
    gap: 40px;
  }
  .spread {
    width: 1000px;
    height: 540px;
    display: flex;
    box-shadow: 0 10px 30px rgba(0,0,0,0.18);
  }
  .panel { width: 500px; height: 100%; position: relative; overflow: hidden; }

  /* Outside: back cover */
  .back-cover { background: linear-gradient(135deg, var(--paper) 0%, var(--paper-shade) 100%); }
  .back-cover .globe-art {
    position: absolute; left: 70px; top: 50px; width: 300px; height: 300px;
    background: radial-gradient(circle at 45% 50%, #e3e6ea 0%, #eef0f3 60%, rgba(238,240,243,0) 72%);
  }
  .back-cover .wordmark {
    position: absolute; left: 0; right: 0; top: 380px; text-align: center;
    display: flex; align-items: center; justify-content: center; gap: 12px;
  }
  .wordmark .dot { width: 18px; height: 18px; border-radius: 50%; background: var(--gold); }
  .wordmark .name { font-weight: 500; letter-spacing: 0.18em; font-size: 24px; color: var(--navy); }
  .contact {
    position: absolute; left: 40px; right: 30px; top: 440px;
    display: flex; justify-content: space-between;
    font-size: 10.5px; font-style: italic; line-height: 1.45;
  }
  .contact ul { list-style: none; }
  .contact li { display: flex; align-items: center; gap: 6px; }
  .contact svg { width: 10px; height: 10px; fill: var(--navy); flex: none; }
  .contact .address { display: flex; gap: 8px; align-items: center; }
  .back-cover .gold-rule { position: absolute; left: 0; right: 0; bottom: 18px; height: 3px; background: var(--gold); }
  .back-cover .navy-band { position: absolute; left: 0; right: 0; bottom: 0; height: 14px; background: var(--navy); }

  /* Outside: front cover */
  .front-cover { background: linear-gradient(160deg, var(--navy) 0%, var(--navy-deep) 100%); }
  .front-cover .wordmark {
    position: absolute; left: 0; right: 0; top: 200px;
    display: flex; align-items: center; justify-content: center; gap: 16px;
  }
  .front-cover .wordmark .dot { width: 26px; height: 26px; }
  .front-cover .wordmark .name { color: var(--paper); font-size: 36px; }

  /* Inside */
  .inside-left { background: var(--paper); border-right: 1px solid #e4e6ea; }
  .inside-right { background: var(--paper); }
  .pocket {
    position: absolute; left: 20px; right: 0; bottom: 0; height: 250px;
    border-top-left-radius: 22px;
    background: linear-gradient(100deg, #b89d60 0%, var(--gold-light) 45%, #b8995a 100%);
  }
</style>
</head>
<body>
  <section class="spread outside">
    <div class="panel back-cover">
      <div class="globe-art" role="img" aria-label="Faint world globe watermark"></div>
      <div class="wordmark"><span class="dot"></span><span class="name">KESTRA REALTY</span></div>
      <div class="contact">
        <ul>
          <li><svg viewBox="0 0 10 10"><path d="M2 0l2 2-1 1.5c.6 1.4 1.6 2.4 3 3L7.5 5.5l2 2L8 9.5C4 9 1 6 .5 2z"/></svg>+ 1 868 555 0147</li>
          <li><svg viewBox="0 0 10 10"><circle cx="5" cy="5" r="4.5" fill="none" stroke="#1c3a68" stroke-width="1"/><path d="M.5 5h9M5 .5v9" stroke="#1c3a68" stroke-width=".8"/></svg>www.kestra-tt.com</li>
          <li><svg viewBox="0 0 10 10"><path d="M0 2h10v6H0z M0 2l5 3.5L10 2" fill="none" stroke="#1c3a68" stroke-width="1"/></svg>info@kestra-tt.com</li>
        </ul>
        <div class="address">
          <svg viewBox="0 0 10 10"><path d="M5 0a3.5 3.5 0 0 1 3.5 3.5C8.5 6 5 10 5 10S1.5 6 1.5 3.5A3.5 3.5 0 0 1 5 0zm0 2a1.5 1.5 0 1 0 0 3 1.5 1.5 0 0 0 0-3z"/></svg>
          <p>Level 1, Marlowe Point Tower<br>4C Seldon Grove Boulevard<br>Marlowe Point, Colwyn Pereira Highway<br>Port of Spain, Trinidad</p>
        </div>
      </div>
      <div class="gold-rule"></div>
      <div class="navy-band"></div>
    </div>
    <div class="panel front-cover">
      <div class="wordmark"><span class="dot"></span><span class="name">KESTRA REALTY</span></div>
    </div>
  </section>

  <section class="spread inside">
    <div class="panel inside-left"></div>
    <div class="panel inside-right">
      <div class="pocket"></div>
    </div>
  </section>
</body>
</html>
```